Creative Brief
Marketing Collateral for Real Estate Business
Create matching postcards and Business Card.
MARKETING COLLATERAL FOR REAL ESTATE COMPANY
Create matching postcards, HTML email template and Business Card.
Postcard (5.5” x 8.5”) template
Email HTML template
Business Card
DESCRIPTION
Our office needs 2-3 “Just Listed” postcard templates for REAL ESTATE FORECLOSURE LISITNGS. The templates must display two logos which are provided (FindMarlowHomesteads.example to be large in size). We need the ability to insert pictures of each new listing inside within the template. The design must be colorful (earth tone colors), professional, simple and eye catching. Postcard: We also want 1-2 generic postcard templates where a standard/general real estate picture is already inserted which can be used for multiple/different properties.
Postcard templates must meet the printing specifications for PressNook.example. The templates must be provided in digital formats that are editable by the project holder. They must also be provided in print ready formats. Our company is based in Charleston, SC, USA. Please view images of Charleston, SC, USA via google if necessary for the postcard template.
The HTML Email Template(s) will be used to mass email our database with new listings.
Real Estate
Buyers of Real Estate Foreclosed Properties; Real Estate Investors.
DESIGN
POSTCARD COMMENTS / STATEMENTS TO BE INCLUDED WITHIN THE POSTCARD / EMAIL HTML
-PRE-LISTING(1-2 Templates)
-JUST LISTED (1-2 Templates)
-SEARCH HUNDREDS OF BANK OWNED FORECLOSURES – SIGN UP FREE! FINDMARLOWHOMESTEADS.EXAMPLE
-Join FindMarlowHomesteads.example and be the first to know about newly listed Charleston Foreclosures.
-Don’t miss this opportunity to buy a bank owned foreclosure.
-We are your Charleston Foreclosure Specialist!
-NEW LISTING ALERT – Sign up and receive listings meeting your criteria today! (in a highlighted icon or box or similar)
-This property is NOT listed in MLS yet. Please contact me if you are interested in purchasing this property. (disclaimer/small font))
POSTCARD SIZE
Postcard 5.5” x 8.5”
COLORS
Blue / Green / Tan (Earth tone colors) / To match FindMarlowHomesteads.example logo
Color (front and back)
Images and Date to be used

```html
<!DOCTYPE html>
<html lang="en">
<head>
<meta charset="utf-8">
<title>FindMarlowHomesteads.example — Postcards, Business Cards and Email Signature</title>
<link href="https://fonts.googleapis.com/css2?family=Roboto+Condensed:wght@400;700;900&family=Open+Sans:wght@400;600;700&display=swap" rel="stylesheet">
<style>
:root{
  --stage:#5a3b22;
  --label:#f3e6cf;
  --blue:#1f5fa8;
  --navy:#16325c;
  --green:#6cb33f;
  --green-dark:#3f8a2a;
  --orange:#f47b20;
  --yellow:#ffe14d;
  --red:#d7261e;
  --tan:#d9c4a0;
  --white:#ffffff;
  --ink:#333333;
  --photo-house:linear-gradient(180deg,#9cc3e6 0%,#c9d9e6 40%,#b59b7a 70%,#6f8f4e 100%);
  --photo-person:linear-gradient(180deg,#e9edf2 0%,#c7a58c 45%,#2b2b33 100%);
}
*{box-sizing:border-box;margin:0;padding:0}
html,body{width:1200px;height:444px;overflow:hidden}
body{background:var(--stage);font-family:"Open Sans",Arial,sans-serif;position:relative;color:var(--ink)}
.label{position:absolute;font:600 9px "Open Sans",Arial,sans-serif;color:var(--label)}
.piece{position:absolute;overflow:hidden;background:var(--white);box-shadow:0 2px 5px rgba(0,0,0,.45)}
.postcard{width:298px;height:190px}
.photo-house{background:var(--photo-house);position:absolute}
.photo-person{background:var(--photo-person);position:absolute}
.brand{position:absolute;display:flex;align-items:center;gap:4px;font:700 9px "Open Sans",Arial,sans-serif;color:var(--blue);white-space:nowrap}
.brand .mark{width:9px;height:9px;background:var(--green);display:inline-block}
.brand.light{color:var(--white)}
.brand.light .mark{background:var(--white)}
.headline{position:absolute;left:10px;top:34px;font-family:"Roboto Condensed",Arial,sans-serif;color:var(--blue);line-height:.95}
.headline .big{display:block;font-weight:900;font-size:25px}
.headline .small{display:block;font-weight:700;font-size:7px;color:var(--green-dark);margin-top:3px}
.front-band{position:absolute;left:0;bottom:0;width:100%;height:38px;background:var(--green);color:var(--white);padding:5px 10px;font-size:6.5px;line-height:1.35}
.front-band .url{font:700 9px "Roboto Condensed",Arial,sans-serif;display:block}
.back-top{position:absolute;left:0;top:0;width:100%;height:24px;background:var(--blue)}
.alert{position:absolute;left:8px;top:29px;padding:3px 8px;background:var(--yellow);color:var(--red);font:900 12px "Roboto Condensed",Arial,sans-serif;border:1.5px solid var(--red)}
.alert.orange{background:var(--orange);color:var(--white);border-color:var(--orange)}
.alert-sub{position:absolute;left:8px;top:50px;font-size:5.5px;line-height:1.25;color:var(--navy);width:144px}
.listing-photo{left:8px;top:67px;width:144px;height:73px}
.miss{position:absolute;left:160px;top:62px;width:128px;font:700 10px "Roboto Condensed",Arial,sans-serif;color:var(--navy);line-height:1.15}
.miss em{font-style:normal;color:var(--red);font-size:12px;display:block}
.mail-lines{position:absolute;left:160px;top:104px;width:128px}
.mail-lines span{display:block;height:1px;background:#b9b9b9;margin-bottom:7px}
.specialist{position:absolute;left:60px;top:146px;width:238px;height:20px;background:var(--navy);color:var(--white);font:700 8.5px "Roboto Condensed",Arial,sans-serif;padding:5px 8px}
.disclaimer{position:absolute;left:62px;top:170px;width:140px;font-size:4.5px;line-height:1.3;color:#666}
.partner{position:absolute;right:8px;top:169px;font:700 8px "Open Sans",Arial,sans-serif;color:var(--navy)}
.card{width:170px;height:92px}
.card .band{position:absolute;left:0;bottom:0;width:100%;height:10px;background:var(--green)}
.card .band.blue{background:var(--blue)}
.card .mini-photo{left:8px;top:30px;width:28px;height:34px}
.card .who{position:absolute;left:42px;top:30px;font-size:6px;line-height:1.35;color:var(--ink)}
.card .who b{display:block;font-size:7.5px;color:var(--navy)}
.card.back{display:flex;align-items:center;justify-content:center;flex-direction:column;gap:3px}
.card.back .partner-name{font:700 11px "Open Sans",Arial,sans-serif}
.card.back .tag{font-size:5.5px;letter-spacing:.5px}
.green-bg{background:var(--green);color:var(--white)}
.blue-bg{background:var(--blue);color:var(--white)}
.navy-bg{background:var(--navy);color:var(--white)}
.white-bg{background:var(--white);color:var(--navy)}
.signature{width:170px;height:92px}
</style>
</head>
<body>

<span class="label" style="left:12px;top:6px">Front</span>
<section class="piece postcard" style="left:12px;top:20px">
  <div class="brand" style="left:10px;top:9px"><span class="mark"></span>FindMarlowHomesteads.example</div>
  <div class="photo-house" style="left:0;top:96px;width:298px;height:56px" role="img" aria-label="Photo of a Charleston house with porch"></div>
  <div class="photo-person" style="left:186px;top:24px;width:104px;height:128px" role="img" aria-label="Photo of the agent holding a flyer"></div>
  <h2 class="headline"><span class="big">SEARCH</span><span class="big">HUNDREDS</span><span class="small">OF BANK OWNED FORECLOSURES</span></h2>
  <p class="front-band"><span class="url">Join FindMarlowHomesteads.example</span>and be the first to know about newly listed Charleston Foreclosures.</p>
</section>

<span class="label" style="left:324px;top:6px">Front</span>
<section class="piece postcard" style="left:324px;top:20px">
  <div class="brand" style="left:10px;top:9px"><span class="mark"></span>FindMarlowHomesteads.example</div>
  <div class="photo-house" style="left:0;top:96px;width:298px;height:56px" role="img" aria-label="Photo of a Charleston house with porch"></div>
  <div class="photo-person" style="left:186px;top:24px;width:104px;height:128px" role="img" aria-label="Photo of the agent holding a flyer"></div>
  <h2 class="headline"><span class="big">SEARCH</span><span class="big">HUNDREDS</span><span class="small">OF BANK OWNED FORECLOSURES</span></h2>
  <p class="front-band"><span class="url">Join FindMarlowHomesteads.example</span>and be the first to know about newly listed Charleston Foreclosures.</p>
</section>

<span class="label" style="left:12px;top:214px">Back</span>
<section class="piece postcard" style="left:12px;top:228px">
  <div class="back-top"></div>
  <div class="brand light" style="left:10px;top:7px"><span class="mark"></span>FindMarlowHomesteads.example</div>
  <div class="alert">NEW LISTING ALERT</div>
  <p class="alert-sub">Sign up and receive listings meeting your criteria today!</p>
  <div class="photo-house listing-photo" role="img" aria-label="Photo of the listed property"></div>
  <p class="miss"><em>DON'T MISS</em>this opportunity to buy a bank owned foreclosure.</p>
  <div class="mail-lines"><span></span><span></span><span></span><span></span></div>
  <div class="photo-person" style="left:8px;top:144px;width:48px;height:46px" role="img" aria-label="Photo of the agent"></div>
  <p class="specialist">We are your Charleston Foreclosure Specialist!</p>
  <p class="disclaimer">This property is NOT listed in MLS yet. Please contact me if you are interested in purchasing this property.</p>
  <span class="partner">Larkfield Realty</span>
</section>

<span class="label" style="left:324px;top:214px">Back</span>
<section class="piece postcard" style="left:324px;top:228px">
  <div class="back-top"></div>
  <div class="brand light" style="left:10px;top:7px"><span class="mark"></span>FindMarlowHomesteads.example</div>
  <div class="alert orange">PRE-LISTING ALERT</div>
  <p class="alert-sub">Sign up and receive listings meeting your criteria today!</p>
  <div class="photo-house listing-photo" role="img" aria-label="Photo of the listed property"></div>
  <p class="miss"><em>DON'T MISS</em>this opportunity to buy a bank owned foreclosure.</p>
  <div class="mail-lines"><span></span><span></span><span></span><span></span></div>
  <div class="photo-person" style="left:8px;top:144px;width:48px;height:46px" role="img" aria-label="Photo of the agent"></div>
  <p class="specialist">We are your Charleston Foreclosure Specialist!</p>
  <p class="disclaimer">This property is NOT listed in MLS yet. Please contact me if you are interested in purchasing this property.</p>
  <span class="partner">Larkfield Realty</span>
</section>

<span class="label" style="left:645px;top:4px">Business Card Front</span>
<section class="piece card" style="left:645px;top:16px">
  <div class="brand" style="left:8px;top:8px;font-size:7px"><span class="mark"></span>FindMarlowHomesteads.example</div>
  <div class="photo-person mini-photo" role="img" aria-label="Agent portrait"></div>
  <p class="who"><b>Lena Ortiz</b>Foreclosure Specialist<br>(555) 014-2290<br>lena@findmarlow.example</p>
  <div class="band"></div>
</section>

<span class="label" style="left:830px;top:4px">Business Card Front</span>
<section class="piece card" style="left:830px;top:16px">
  <div class="brand" style="left:8px;top:8px;font-size:7px"><span class="mark"></span>FindMarlowHomesteads.example</div>
  <div class="photo-person mini-photo" role="img" aria-label="Agent portrait"></div>
  <p class="who"><b>Lena Ortiz</b>Foreclosure Specialist<br>(555) 014-2290<br>lena@findmarlow.example</p>
  <div class="band blue"></div>
</section>

<span class="label" style="left:1015px;top:4px">Business Card Front</span>
<section class="piece card" style="left:1015px;top:16px">
  <div class="brand" style="left:8px;top:8px;font-size:7px"><span class="mark"></span>FindMarlowHomesteads.example</div>
  <p class="who" style="left:10px;top:34px"><b>Lena Ortiz</b>Foreclosure Specialist<br>(555) 014-2290<br>lena@findmarlow.example</p>
  <div class="band"></div>
</section>

<span class="label" style="left:645px;top:110px">Business Card Back</span>
<section class="piece card back green-bg" style="left:645px;top:122px">
  <span class="partner-name">Larkfield Realty</span><span class="tag">FINDMARLOWHOMESTEADS.EXAMPLE</span>
</section>

<span class="label" style="left:830px;top:110px">Business Card Back</span>
<section class="piece card back navy-bg" style="left:830px;top:122px">
  <span class="partner-name">Larkfield Realty</span><span class="tag">FINDMARLOWHOMESTEADS.EXAMPLE</span>
</section>

<span class="label" style="left:1015px;top:110px">Business Card Front</span>
<section class="piece card" style="left:1015px;top:122px">
  <div class="brand" style="left:8px;top:8px;font-size:7px"><span class="mark"></span>FindMarlowHomesteads.example</div>
  <div class="photo-person mini-photo" role="img" aria-label="Agent portrait"></div>
  <p class="who"><b>Lena Ortiz</b>Foreclosure Specialist<br>(555) 014-2290<br>lena@findmarlow.example</p>
  <div class="band blue"></div>
</section>

<span class="label" style="left:645px;top:216px">Business Card Back</span>
<section class="piece card back white-bg" style="left:645px;top:228px">
  <span class="partner-name">Larkfield Realty</span><span class="tag">FINDMARLOWHOMESTEADS.EXAMPLE</span>
</section>

<span class="label" style="left:830px;top:216px">Business Card Back</span>
<section class="piece card back blue-bg" style="left:830px;top:228px">
  <span class="partner-name">Larkfield Realty</span><span class="tag">FINDMARLOWHOMESTEADS.EXAMPLE</span>
</section>

<span class="label" style="left:1015px;top:216px">Business Card Back</span>
<section class="piece card back green-bg" style="left:1015px;top:228px">
  <span class="partner-name">Larkfield Realty</span><span class="tag">FINDMARLOWHOMESTEADS.EXAMPLE</span>
</section>

<span class="label" style="left:645px;top:322px">Email Signature</span>
<section class="piece signature" style="left:645px;top:334px">
  <div class="brand" style="left:8px;top:8px;font-size:7px"><span class="mark"></span>FindMarlowHomesteads.example</div>
  <div class="photo-person" style="left:8px;top:28px;width:28px;height:34px" role="img" aria-label="Agent portrait"></div>
  <p style="position:absolute;left:42px;top:28px;font-size:6px;line-height:1.35">
    <b style="display:block;font-size:7.5px;color:var(--navy)">Lena Ortiz</b>Foreclosure Specialist<br>
    <span style="display:inline-flex;align-items:center;gap:3px"><svg width="6" height="6" viewBox="0 0 10 10"><path d="M2 1l2 2-1 1.5c.7 1.3 1.7 2.3 3 3L7.5 6l2 2-1.5 1.5C4.5 9 1 5.5.5 1.5z" fill="#1f5fa8"/></svg>(555) 014-2290</span><br>
    lena@findmarlow.example
  </p>
  <div style="position:absolute;left:0;bottom:0;width:100%;height:10px;background:var(--green)"></div>
</section>

</body>
</html>
```